Christmas Party Poster

I am promoting a Christmas Party for teenagers age 13-17 years old. The event is the first of its kind in our area, Weston Super Mare. The ticket price is to include food, soft drink's, music, entertainment.

There is nothing else of its kind in the the area or surrounding towns so a one of a kind event and new to the town. I would like the poster to be as simple and less busy as possible while still clearly showing the key information, anything that can be added it to show its a Christmas party for teenagers would be great. Also this is aimed at 13-17 year old's so as current and modern a design as possible.
Updates

A big thank you for the designs so far, As this is my first project I'm just getting the hang of what to ask for. I have slightly updated the brief and I now realize less is more, so long as the poster has the key elements of event name, date, time's, location, price and age range. The rest I should have been more flexible on. Thank you for your patience.

Target Market(s)

My Target Market are teenagers specifically 13-17 year olds

Industry/Entity Type

Town

Requirements
Must have
• The Title 'Frostlark' The venue is 'The Amber Pavilion w-s-m', Phone Number '01934 582093' Date '19th December'. Times '19.00 - 23.00'. Strictly u18 or age 13-17 years. Ticket price of £20. Face book 'frost lark wsm' limited 4 tickets per person
Nice to have
• Christmas Party, Photo of your night out. Food and drink included
Should not have
• no worded reference to Santa, snowmen, reindeer, disco, try to keep out as not to offend cool teenagers.

```html
<!DOCTYPE html>
<html lang="en">
<head>
<meta charset="utf-8">
<title>Frostlark – Christmas Party</title>
<link rel="stylesheet" href="https://fonts.googleapis.com/css2?family=Boogaloo&family=Schoolbell&display=swap">
<style>
  :root {
    --page-bg: #d6d6d6;
    --night: #1b1b1d;
    --night-soft: #2a2a2e;
    --snow: #f4f4f4;
    --ice-blue: #3db8e4;
    --band-grey: #8a8a8a;
    --font-script: "Schoolbell", cursive;
    --font-display: "Boogaloo", sans-serif;
  }
  * { box-sizing: border-box; margin: 0; padding: 0; }
  html, body {
    width: 1200px; height: 800px; overflow: hidden;
    background: var(--page-bg);
  }
  .poster {
    position: absolute; left: 380px; top: 70px;
    width: 440px; height: 660px;
    background: var(--night);
    overflow: hidden;
    color: var(--snow);
    text-align: center;
  }
  .snowfield {
    position: absolute; inset: 0;
    background: radial-gradient(ellipse at 50% 40%, var(--night-soft), var(--night));
  }
  .poster-content { position: relative; height: 100%; }
  .eyebrow {
    padding-top: 26px;
    font-family: var(--font-display);
    font-size: 24px; letter-spacing: 1px;
    color: var(--ice-blue);
  }
  .event-title {
    font-family: var(--font-script);
    font-size: 86px; line-height: 1; font-weight: 400;
    color: transparent;
    -webkit-text-stroke: 2px var(--snow);
    margin-top: 4px;
  }
  .date-band {
    margin-top: 22px;
    background: var(--band-grey);
    height: 62px; line-height: 62px;
    font-family: var(--font-script);
    font-size: 38px; color: var(--snow);
  }
  .venue {
    margin-top: 20px;
    font-family: var(--font-display);
    font-size: 33px; letter-spacing: 0.5px;
  }
  .rule {
    width: 330px; height: 2px; margin: 8px auto 0;
    background: var(--ice-blue);
  }
  .times {
    margin-top: 16px;
    font-family: var(--font-display);
    font-size: 40px; letter-spacing: 1px;
  }
  .age {
    font-family: var(--font-display);
    font-size: 28px; margin-top: 2px;
  }
  .price {
    margin-top: 22px;
    font-family: var(--font-display);
    color: var(--snow);
    font-size: 22px;
  }
  .price-amount {
    font-family: var(--font-script);
    font-size: 66px; color: var(--ice-blue);
    vertical-align: middle; margin-right: 8px;
  }
  .included {
    font-family: var(--font-display);
    font-size: 26px; color: var(--ice-blue);
    margin-top: -4px;
  }
  .contact {
    margin-top: 28px;
    display: flex; justify-content: center; align-items: baseline; gap: 14px;
  }
  .contact-label {
    font-family: var(--font-display);
    font-size: 22px; color: var(--ice-blue);
  }
  .contact-number {
    font-family: var(--font-script);
    font-size: 52px; color: var(--snow);
    letter-spacing: 2px;
  }
</style>
</head>
<body>
  <main class="poster">
    <div class="snowfield" role="img" aria-label="Snow falling across a dark night sky"></div>
    <div class="poster-content">
      <p class="eyebrow">CRISTMAS PARTY</p>
      <h1 class="event-title">Frostlark</h1>
      <p class="date-band">19th December</p>
      <p class="venue">The Amber Pavilion W-S-M</p>
      <div class="rule"></div>
      <p class="times">FROM 19.00 TO 23.00</p>
      <p class="age">AGE 13-17</p>
      <p class="price"><span class="price-amount">£20</span>ticket</p>
      <p class="included">Food and drink included</p>
      <p class="contact">
        <span class="contact-label">call us</span>
        <span class="contact-number">01934 582093</span>
      </p>
    </div>
  </main>
</body>
</html>
```